Business Card Design for a technology company

Our current business card is outdated and stale.

We need a new look and one soon.

We're a telematics (GPS tracking) company based in Australia. Our audiences are transport and logistics company.

Target Market(s)

1. Transport and Logistics Companies
2. Food and Beverage Manufacturers
3. Concrete Businesses

Industry/Entity Type

Logistics

Contact Information for Business Card

Halvor Pinet

Font styles to use
Sans Serif

Colors
3276b5
0255a3
85acd3
cfdeed
ffffff

Requirements
Must have
• Logo
• "Premium Suppliers of Real Time Temperature Tracking"
• Contact Name
• Business Title
• Address
• Telephone
• Mobile
• Email
• Website URL
Nice to have
• Visual representation of tracking or maps.
Should not have
• Image of a satellite as currently shown

```html
<!DOCTYPE html>
<html lang="en">
<head>
<meta charset="utf-8">
<title>Halvor Pinet – Business Card</title>
<link href="https://fonts.googleapis.com/css2?family=Open+Sans:wght@400;600;700;800&display=swap" rel="stylesheet">
<style>
  :root {
    --brand-blue: #0b4c9c;
    --brand-blue-dark: #0255a3;
    --ink: #1b1b1b;
    --paper: #ffffff;
    --stage: #eef1f5;
    --map-light: #e9e4d8;
    --map-mid: #cfd9c4;
  }
  * { box-sizing: border-box; margin: 0; padding: 0; }
  html, body { width: 1200px; height: 1200px; overflow: hidden; }
  body {
    background: var(--stage);
    font-family: "Open Sans", Arial, sans-serif;
    display: flex; flex-direction: column; align-items: center; justify-content: center;
    gap: 40px;
  }
  .card {
    width: 960px; height: 540px; position: relative; overflow: hidden;
    box-shadow: 0 6px 20px rgba(0,0,0,.15);
  }

  /* Front */
  .card-front { background: var(--brand-blue); }
  .front-brand {
    position: absolute; left: 120px; top: 230px;
    display: flex; align-items: center; gap: 18px;
  }
  .brand-dot { width: 44px; height: 44px; border-radius: 50%; background: var(--paper); flex: none; }
  .front-brand .brand-name {
    color: var(--paper); font-weight: 800; font-size: 88px; letter-spacing: -2px; line-height: 1;
    white-space: nowrap;
  }
  .front-url {
    position: absolute; left: 192px; top: 340px;
    color: var(--paper); font-size: 20px; font-weight: 600;
  }
  .map-ribbon { position: absolute; right: 90px; top: 0; }

  /* Back */
  .card-back { background: var(--paper); }
  .back-brand {
    position: absolute; left: 60px; top: 140px;
    display: flex; align-items: center; gap: 16px;
  }
  .back-brand .brand-dot { background: var(--brand-blue); width: 36px; height: 36px; }
  .back-brand .brand-name {
    color: var(--brand-blue); font-weight: 800; font-size: 76px; letter-spacing: -2px; line-height: 1;
    white-space: nowrap;
  }
  .person { position: absolute; left: 660px; top: 70px; }
  .person-name { color: var(--brand-blue-dark); font-weight: 700; font-size: 30px; line-height: 1.1; white-space: nowrap; }
  .person-title { color: var(--ink); font-weight: 700; font-size: 18px; }
  .bands { position: absolute; left: 0; top: 290px; }
  .contact-list {
    position: absolute; left: 40px; top: 308px; list-style: none;
    color: var(--paper); font-size: 21px; line-height: 36px;
  }
  .contact-list li { display: flex; align-items: center; gap: 14px; white-space: nowrap; }
  .contact-list svg { width: 20px; height: 20px; fill: var(--paper); flex: none; }
  .web {
    position: absolute; left: 718px; top: 366px;
    color: var(--paper); font-size: 17px; display: flex; align-items: center; gap: 10px;
    white-space: nowrap;
  }
  .web svg { width: 18px; height: 18px; flex: none; }
  .tagline {
    position: absolute; left: 0; right: 0; top: 492px; text-align: center;
    color: var(--brand-blue-dark); font-weight: 700; font-size: 18px; letter-spacing: 3.5px;
    text-transform: uppercase; white-space: nowrap;
  }
</style>
</head>
<body>

<section class="card card-front">
  <div class="front-brand">
    <span class="brand-dot"></span>
    <span class="brand-name">Halvor Pinet</span>
  </div>
  <div class="front-url">www.halvorpinet.com.au</div>
  <svg class="map-ribbon" width="170" height="230" viewBox="0 0 170 230" role="img" aria-label="Street map with a tracked route ending at a location pin">
    <defs>
      <linearGradient id="mapTone" x1="0" y1="0" x2="1" y2="1">
        <stop offset="0" stop-color="var(--map-mid)"/>
        <stop offset="1" stop-color="var(--map-light)"/>
      </linearGradient>
    </defs>
    <path d="M0 0 H170 V230 L85 180 L0 230 Z" fill="url(#mapTone)"/>
  </svg>
</section>

<section class="card card-back">
  <div class="back-brand">
    <span class="brand-dot"></span>
    <span class="brand-name">Halvor Pinet</span>
  </div>
  <div class="person">
    <div class="person-name">Dorian Kessel</div>
    <div class="person-title">Manager</div>
  </div>

  <svg class="bands" width="960" height="180" viewBox="0 0 960 180">
    <polygon points="0,0 600,0 660,90 600,180 0,180" fill="var(--brand-blue)"/>
    <polygon points="640,0 960,0 960,180 640,180 700,90" fill="var(--ink)"/>
  </svg>

  <ul class="contact-list">
    <li><svg viewBox="0 0 24 24"><path d="M12 2a7 7 0 0 0-7 7c0 5 7 13 7 13s7-8 7-13a7 7 0 0 0-7-7zm0 9.5a2.5 2.5 0 1 1 0-5 2.5 2.5 0 0 1 0 5z"/></svg>4, 18 Carrow Street, Elmhurst VIC 3162</li>
    <li><svg viewBox="0 0 24 24"><path d="M6.6 10.8a15 15 0 0 0 6.6 6.6l2.2-2.2a1 1 0 0 1 1-.25 11.4 11.4 0 0 0 3.6.57 1 1 0 0 1 1 1V20a1 1 0 0 1-1 1A17 17 0 0 1 3 4a1 1 0 0 1 1-1h3.5a1 1 0 0 1 1 1c0 1.25.2 2.45.57 3.6a1 1 0 0 1-.25 1z"/></svg>+61 3 9041 2276</li>
    <li><svg viewBox="0 0 24 24"><path d="M6 3h9v5H6zM3 9h18v12H3zm4 3v2h2v-2zm4 0v2h2v-2zm4 0v2h2v-2zm-8 4v2h2v-2zm4 0v2h2v-2zm4 0v2h2v-2z"/></svg>+61 3 9041 2276</li>
    <li><svg viewBox="0 0 24 24"><path d="M2 5h20v14H2zm2 2v.5l8 5 8-5V7l-8 5z"/></svg>dkessel@halvorpinet.com.au</li>
  </ul>

  <div class="web">
    <svg viewBox="0 0 24 24" fill="none" stroke="#fff" stroke-width="2"><circle cx="12" cy="12" r="9"/><path d="M3 12h18M12 3c3 3 3 15 0 18M12 3c-3 3-3 15 0 18"/></svg>
    www.halvorpinet.com.au
  </div>

  <div class="tagline">Premium Suppliers of Real Time Temperature Tracking</div>
</section>

</body>
</html>
```